need professional, precise design for a website

I will start with a homepage design and if we pick your design, we'll have you design up to 6 more interior pages (we'll pay extra for these of course). We need a homepage design for a reserve study company based in Idaho, covering the northwest region. The company is called copper ridge reserve study. Their current site is at https://www.copperridgereserves.example/ and they really like this site for inspiration https://www.fundplannerhub.example/ but they would like an original design, just more modern and fresh like the sample site. I have logo files I will attach. They want something that looks financial and has a feel of accuity. Their main call to action will be to have someone fill in a contact form or call them on the phone. They will have a sample study that someone can download as on the fundplannerhub site. You can use copy from their current site.

```html
<!DOCTYPE html>
<html lang="en">
<head>
<meta charset="utf-8">
<title>Copper Ridge Reserves — Reserve Studies</title>
<link href="https://fonts.googleapis.com/css2?family=Barlow+Condensed:wght@200;300;400;500;600;700&display=swap" rel="stylesheet">
<style>
  :root {
    --navy: #0b1a3a;
    --navy-soft: rgba(40, 52, 82, 0.72);
    --blue: #1677f2;
    --white: #ffffff;
    --grey-band: #f3f3f5;
    --ink: #1b2235;
    --muted: #5b6172;
  }
  * { margin: 0; padding: 0; box-sizing: border-box; }
  html, body { width: 770px; height: 1200px; overflow: hidden; }
  body { font-family: "Barlow Condensed", sans-serif; color: var(--ink); background: var(--white); position: relative; }

  .hero { position: absolute; left: 0; top: 0; width: 770px; height: 482px; overflow: hidden; }
  .hero-photo {
    position: absolute; inset: 0;
    background:
      radial-gradient(ellipse at 50% 10%, rgba(214,224,238,0.9) 0%, rgba(150,168,196,0.5) 30%, transparent 60%),
      linear-gradient(180deg, #8ea3c2 0%, #4a5d7e 35%, #1f2b44 65%, #121a2c 100%);
  }
  .site-header {
    position: absolute; left: 0; top: 0; width: 770px; height: 46px;
    background: rgba(60, 74, 104, 0.55);
    display: flex; align-items: center; justify-content: space-between; padding: 0 28px 0 30px;
  }
  .brand { display: flex; align-items: center; gap: 6px; color: var(--white); font-size: 15px; font-weight: 400; letter-spacing: 0.5px; }
  .brand-dot { width: 14px; height: 14px; border: 1.5px solid var(--white); border-radius: 50%; }
  .main-nav { display: flex; gap: 14px; }
  .main-nav a { color: var(--white); text-decoration: none; font-size: 8px; letter-spacing: 0.3px; text-transform: uppercase; padding-bottom: 2px; }
  .main-nav a.is-active { border-bottom: 1px solid var(--white); }

  .call-button {
    position: absolute; left: 633px; top: 85px; width: 137px; height: 32px;
    background: var(--blue); color: var(--white); font-size: 17px; font-weight: 500;
    display: flex; align-items: center; justify-content: center; text-decoration: none;
  }
  .headline-box {
    position: absolute; left: 208px; top: 187px; width: 355px; height: 105px;
    background: var(--navy-soft); color: var(--white); text-align: right; padding: 14px 16px 0 0;
    text-transform: uppercase;
  }
  .headline-box .line-light { font-weight: 200; font-size: 35px; line-height: 40px; letter-spacing: 0.3px; }
  .headline-box .line-bold { font-weight: 700; font-size: 36px; line-height: 44px; }
  .quote-button {
    position: absolute; left: 317px; top: 305px; width: 114px; height: 28px;
    border: 1.5px solid var(--white); color: var(--white); font-size: 10.5px; font-weight: 600;
    display: flex; align-items: center; justify-content: center; text-decoration: none; text-transform: uppercase;
  }
  .slide-dots { position: absolute; left: 22px; top: 446px; display: flex; align-items: center; gap: 5px; color: var(--white); }
  .slide-dots .dot { width: 5px; height: 5px; border-radius: 50%; background: var(--white); }
  .slide-dots .dot.is-current { width: 14px; border-radius: 3px; }
  .slide-dots .count { font-size: 15px; font-weight: 300; margin-left: 6px; }
  .slide-arrows { position: absolute; left: 587px; top: 436px; display: flex; }
  .slide-arrows .arrow { width: 92px; height: 46px; display: flex; align-items: center; justify-content: center; }
  .slide-arrows .prev { background: var(--white); }
  .slide-arrows .next { background: var(--navy); width: 91px; }

  .service { position: absolute; left: 0; width: 770px; height: 229px; }
  .service.band-grey { background: var(--grey-band); }
  .service.band-white { background: var(--white); }
  .service-photo {
    position: absolute; top: 46px; width: 230px; height: 137px;
    background: linear-gradient(160deg, #c9d4e4 0%, #6f819e 30%, #1e2638 62%, #3a2c22 88%, #6a4a2c 100%);
  }
  .service-copy { position: absolute; width: 232px; }
  .service-title { font-size: 15px; font-weight: 300; text-transform: uppercase; color: var(--ink); margin-bottom: 7px; letter-spacing: 0.2px; }
  .service-title strong { font-weight: 700; }
  .service-text { font-size: 7.3px; line-height: 10.2px; color: var(--muted); font-weight: 400; }
  .align-right { text-align: right; }

  .site-footer {
    position: absolute; left: 0; top: 1170px; width: 770px; height: 30px; background: var(--navy);
    color: var(--white); font-size: 7px; display: flex; align-items: center; justify-content: center;
  }
</style>
</head>
<body>
  <section class="hero">
    <div class="hero-photo" role="img" aria-label="Upward view of glass office towers against a pale sky"></div>
    <header class="site-header">
      <div class="brand"><span class="brand-dot"></span>Copper Ridge Reserves</div>
      <nav class="main-nav">
        <a href="#" class="is-active">Home</a>
        <a href="#">About Our Company</a>
        <a href="#">Reserve Studies</a>
        <a href="#">Contact Us</a>
      </nav>
    </header>
    <a class="call-button" href="#">CALL (208) 555-0143</a>
    <div class="headline-box">
      <div class="line-light">Your Financial Road Map</div>
      <div class="line-bold">For the Next 30 Years!</div>
    </div>
    <a class="quote-button" href="#">Request a Quote</a>
    <div class="slide-dots">
      <span class="dot is-current"></span><span class="dot"></span><span class="dot"></span><span class="dot"></span><span class="dot"></span>
      <span class="count">01</span>
    </div>
    <div class="slide-arrows">
      <div class="arrow prev">
        <svg width="22" height="14" viewBox="0 0 22 14"><path d="M21 7H2M8 1L2 7l6 6" fill="none" stroke="#0b1a3a" stroke-width="2"/></svg>
      </div>
      <div class="arrow next">
        <svg width="22" height="14" viewBox="0 0 22 14"><path d="M1 7h19M14 1l6 6-6 6" fill="none" stroke="#ffffff" stroke-width="2"/></svg>
      </div>
    </div>
  </section>

  <section class="service band-grey" style="top:482px">
    <div class="service-photo" style="left:144px" role="img" aria-label="Glass office towers seen from street level"></div>
    <div class="service-copy" style="left:397px; top:93px">
      <h2 class="service-title"><strong>HOA</strong> &amp; Condominium Studies</h2>
      <p class="service-text">Every homeowners association is different. Different sets of assets, different financials and different historical backgrounds that have brought you to the present. Each of these is taken into consideration to customize your 30 year budget and build the most accurate, most precise long-term savings ("reserve") report you can buy.</p>
    </div>
  </section>

  <section class="service band-white" style="top:711px">
    <div class="service-photo" style="left:397px" role="img" aria-label="Glass office towers seen from street level"></div>
    <div class="service-copy align-right" style="left:142px; top:86px">
      <h2 class="service-title">Commercial, Vacation &amp; <strong>Time Share</strong></h2>
      <p class="service-text">Your property represents a significant capital investment. In many cases, your business is dependent on the livelihood and functionality of the edifice in which it resides. We believe a fiscally sound plan and budget of capital expenses is as essential as the building itself. We are comprehensive, thorough and intense about our calculations.</p>
    </div>
  </section>

  <section class="service band-grey" style="top:940px">
    <div class="service-photo" style="left:144px" role="img" aria-label="Glass office towers seen from street level"></div>
    <div class="service-copy" style="left:397px; top:86px">
      <h2 class="service-title"><strong>Parks</strong> &amp; Public Lands</h2>
      <p class="service-text">Much like HOA's and condominiums, you have finite funds that originate from a constituent base of tax payers. Planning the use of these funds and repairs and/or maintenance of public assets is essential to transparency and candid communication with your constituents. Being in control of the future starts with a financial plan.</p>
    </div>
  </section>

  <footer class="site-footer">Copyright Copper Ridge Reserves, LLC © 2017 All Rights Reserved</footer>
</body>
</html>
```